Direct to Consumer extended service contract business with a new disruptive business model needs a

We need a customized wordpress design for a company called 'Bright Harbor Assurance'.
We provide an innovative and unique service contract protection program direct to consumers. This program provides monthly coverage for all electronics purchased in the last 4 years and all electronics the consumer purchases in the future for a low monthly fee. The overall design should communicate a sense of legitimacy, ethics, and superior customer service and support (in an industry that has a huge PR issue to overcome).
Electronics is the first product group, other product groups with different price points to launch in the future..

Target Market(s)

All purchasers of electronic goods...all demographics

Industry/Entity Type

Electronics

Font styles to use
Sans Serif

Requirements
Must have
• Customer Testimonials
Industry News
Customer ratings
Blog posts
Call to action messaging
Like the functional elements and design of veltomarket.example (need to be better)
Nice to have
• Like to see video testimonials
Social network "whats trending related to electronics or service contract industry"
Easy way to register products for warranty

```html
<!DOCTYPE html>
<html lang="en">
<head>
<meta charset="utf-8">
<title>Bright Harbor Assurance</title>
<link rel="stylesheet" href="https://fonts.googleapis.com/css2?family=PT+Sans:ital,wght@0,400;0,700;1,400;1,700&family=Roboto+Condensed:ital,wght@0,400;0,700;1,700&display=swap">
<style>
:root{
  --red:#e31b23;
  --red-dark:#c3141b;
  --black:#000;
  --band:#1e1e20;
  --hero:#252526;
  --white:#fff;
  --ink:#111;
  --grey:#8a8a8a;
  --rule:#bdbdbd;
  --star-red:#e31b23;
  --star-blue:#2a8be0;
  --star-green:#7ac231;
}
*{box-sizing:border-box;margin:0;padding:0}
html,body{width:1200px;height:2748px;overflow:hidden;background:var(--white)}
body{position:relative;font-family:"PT Sans",Arial,sans-serif;color:var(--ink)}
.abs{position:absolute}
/* header */
.site-header{left:0;top:0;width:1200px;height:119px;background:var(--black)}
.top-links{right:26px;top:8px;display:flex;gap:26px;font:700 15px "PT Sans",sans-serif;color:var(--white)}
.brand{left:48px;top:40px;color:var(--red);font:400 48px/1 "PT Sans",sans-serif;letter-spacing:4px}
.brand-tag{left:48px;top:90px;color:var(--white);font:700 16px "PT Sans",sans-serif;letter-spacing:.5px}
.main-nav{right:26px;top:63px;display:flex;gap:24px;font:700 19px "PT Sans",sans-serif;color:var(--white)}
.main-nav .active{color:var(--red);border-bottom:2px solid var(--red);padding-bottom:2px}
/* hero */
.hero{left:0;top:119px;width:1200px;height:531px;background:var(--hero)}
.hero-device{left:55px;top:55px;width:559px;height:339px;background:linear-gradient(180deg,#d9dbde,#a7abb0);border-radius:10px}
.slogan{right:92px;display:block;text-align:right}
.slogan span{background:var(--black);color:var(--white);font:700 37px/1 "PT Sans",sans-serif;letter-spacing:1.5px;padding:5px 8px;display:inline-block}
.cta{left:663px;top:282px;width:445px;height:57px;background:var(--red);color:var(--white);font:700 40px/57px "PT Sans",sans-serif;text-align:center;box-shadow:0 3px 0 var(--red-dark)}
/* features */
.features{left:101px;top:568px;width:998px;height:202px;background:var(--white);display:flex;gap:9px;padding:18px 14px 0}
.feature{width:318px}
.feature-head{height:70px;background:var(--red);display:flex;align-items:center;gap:14px;padding:0 12px;color:var(--white);font:700 23px/1.05 "PT Sans",sans-serif}
.feature-head svg{flex:none}
.feature ul{list-style:none;margin-top:12px;font:15px/1.35 "PT Sans",sans-serif;padding-left:10px}
/* band sections */
.band{left:0;width:1200px;background:var(--band)}
.title{width:1200px;text-align:center;font:700 italic 31px "Roboto Condensed",sans-serif}
.title.light{color:var(--white)}
.title.red{color:var(--red)}
.arrow{width:0;height:0;border-top:17px solid transparent;border-bottom:17px solid transparent}
.arrow.left{border-right:17px solid var(--white)}
.arrow.right{border-left:17px solid var(--white)}
.rating{display:flex;gap:16px;align-items:flex-start;color:var(--white)}
.store-mark{width:95px;height:95px;border-radius:50%;flex:none}
.rating h3{font:700 28px/1.1 "PT Sans",sans-serif}
.rating p{font:19px/1.25 "PT Sans",sans-serif}
.stars{display:flex;gap:6px;margin-top:6px}
/* cards */
.card{width:317px}
.card .photo{height:234px}
.card h4{font:700 24px/1 "PT Sans",sans-serif;margin-top:14px;letter-spacing:.3px}
.card .meta{font:700 italic 12px "PT Sans",sans-serif;color:var(--red);margin-top:4px}
.card .meta.thin{font-weight:400}
.card hr{border:0;border-top:1px solid var(--rule);margin:10px 0 10px}
.card p{font:italic 13px/1.5 "PT Sans",sans-serif;color:var(--grey)}
.video{width:337px;height:187px;border:1px solid #5b6b7e;background:linear-gradient(135deg,#123b6e,#0a2245)}
.play{left:140px;top:64px;width:58px;height:58px;border-radius:50%;background:#6cbf2c;border:3px solid #fff}
.play::after{content:"";position:absolute;left:20px;top:13px;border-left:20px solid #fff;border-top:13px solid transparent;border-bottom:13px solid transparent}
/* footer */
.footer{left:0;top:2468px;width:1200px;height:247px;background:var(--band);color:var(--white)}
.foot-brand{left:95px;top:30px;font:400 44px/1 "PT Sans",sans-serif;letter-spacing:4px}
.foot-links{top:118px;display:flex;flex-direction:column;gap:5px;font:19px/1.25 "PT Sans",sans-serif}
.feed-title{left:420px;top:22px;font:700 italic 31px "Roboto Condensed",sans-serif}
.social{top:22px;width:36px;height:36px;border-radius:4px}
.feed{left:420px;top:75px;width:313px;height:159px;background:var(--white);padding:12px 16px}
.feed-item{display:flex;gap:12px;align-items:center;margin-bottom:10px}
.feed-item i{width:36px;height:36px;border-radius:50%;background:var(--red);flex:none}
.feed-item b{display:block;color:var(--red);font:700 10px "PT Sans",sans-serif}
.feed-item span{font:700 10px "PT Sans",sans-serif;color:#222}
.contact-title{left:824px;top:30px;display:flex;align-items:center;gap:12px;font:700 26px "Roboto Condensed",sans-serif}
.contact-rule{left:886px;top:70px;width:232px;border-top:2px solid var(--white)}
.contact-list{left:886px;top:88px;font:italic 19px/1.5 Arial,"PT Sans",sans-serif;width:310px;white-space:nowrap}
.contact-list b{font-weight:700}
.copyright{left:0;top:2715px;width:1200px;height:33px;background:var(--black);color:var(--white);text-align:center;font:700 14px/33px "PT Sans",sans-serif}
</style>
</head>
<body>

<header class="site-header abs">
  <nav class="top-links abs"><span>Login</span><span>Support</span><span>Call: 555-014-2290</span></nav>
  <div class="brand abs">KESTREL</div>
  <div class="brand-tag abs">Bright Harbor Assurance</div>
  <nav class="main-nav abs">
    <span class="active">HOME</span><span>PLANS</span><span>BENEFITS</span><span>ABOUT US</span><span>BLOG</span><span>NEWS</span><span>CONTACT</span>
  </nav>
</header>

<section class="hero abs">
  <div class="hero-device abs" role="img" aria-label="Laptop showing the quote form and store ratings"></div>
  <div class="slogan abs" style="top:114px"><span>BUYS YOUR DEVICE</span></div>
  <div class="slogan abs" style="top:164px"><span>PAY MONTHLY TO SECURE</span></div>
  <div class="slogan abs" style="top:214px"><span>CLAIM/FIX YOUR DEVICE</span></div>
  <div class="cta abs">GET FREE QUOTE</div>
</section>

<section class="features abs">
  <div class="feature">
    <div class="feature-head">
      <svg width="44" height="40" viewBox="0 0 44 40"><rect x="4" y="12" width="36" height="20" rx="10" fill="#fff"/></svg>
      <span>PURCHASE IN LOW<br>RATES</span>
    </div>
    <ul><li>- 1000 products available online</li><li>- Low as price as compare to market price</li><li>- Easy to purchase any product</li></ul>
  </div>
  <div class="feature">
    <div class="feature-head">
      <svg width="44" height="48" viewBox="0 0 44 48"><path d="M22 2 L40 8 V22 C40 34 32 42 22 46 C12 42 4 34 4 22 V8 Z" fill="#fff"/></svg>
      <span>PROTECT DEVICES<br>BY PAYING MONTHY</span>
    </div>
    <ul><li>- Pay montly fee</li><li>- Low rates as compate to others</li><li>- Secure your device in advance</li></ul>
  </div>
  <div class="feature">
    <div class="feature-head">
      <svg width="44" height="40" viewBox="0 0 44 40" fill="none" stroke="#fff" stroke-width="4"><path d="M8 16 V10 H34 M28 4 L34 10 L28 16"/><path d="M36 24 V30 H10 M16 24 L10 30 L16 36"/></svg>
      <span>CLAIM AND FIX<br>YOUR DEVICE</span>
    </div>
    <ul><li>- Claim your money you have paid</li><li>- Fix your broken devices</li><li>- Fast and reliable</li></ul>
  </div>
</section>

<section class="band abs" style="top:771px;height:282px">
  <h2 class="title light abs" style="top:28px">Customer Raiting</h2>
  <div class="arrow left abs" style="left:24px;top:153px"></div>
  <div class="arrow right abs" style="left:1107px;top:153px"></div>
  <div class="rating abs" style="left:73px;top:123px">
    <div class="store-mark" style="background:#2b2b2b;border:4px solid var(--red)"></div>
    <div><h3>Orchard Store</h3><p>some info came here<br>with description.</p>
      <div class="stars"><svg width="140" height="24"><g fill="var(--star-red)"><polygon id="s" points="12,0 15,8 24,8 17,13 20,22 12,17 4,22 7,13 0,8 9,8"/><use href="#s" x="29"/><use href="#s" x="58"/><use href="#s" x="87"/><use href="#s" x="116"/></g></svg></div></div>
  </div>
  <div class="rating abs" style="left:425px;top:123px">
    <div class="store-mark" style="background:#1e1e20;border:3px dashed var(--white)"></div>
    <div><h3>Riverline Store</h3><p>some info came here<br>with description.</p>
      <div class="stars"><svg width="140" height="24"><g fill="var(--star-blue)"><use href="#s"/><use href="#s" x="29"/><use href="#s" x="58"/><use href="#s" x="87"/><use href="#s" x="116"/></g></svg></div></div>
  </div>
  <div class="rating abs" style="left:785px;top:123px">
    <div class="store-mark" style="background:var(--red)"></div>
    <div><h3>Globe Store</h3><p>some info came here<br>with description.</p>
      <div class="stars"><svg width="140" height="24"><g fill="var(--star-green)"><use href="#s"/><use href="#s" x="29"/><use href="#s" x="58"/><use href="#s" x="87"/><use href="#s" x="116"/></g></svg></div></div>
  </div>
</section>

<section class="abs" style="left:0;top:1053px;width:1200px;height:559px">
  <h2 class="title red abs" style="top:40px">Industry News</h2>
  <article class="card abs" style="left:115px;top:105px">
    <div class="photo" role="img" aria-label="Shopper testing a laptop in an electronics store" style="background:linear-gradient(135deg,#9fb6cf,#3f5f85)"></div>
    <h4>Lorem ipsum nipsum saye</h4><div class="meta">Posted on: Sep 29th, 2014</div><hr>
    <p>Lorem ipsum nipsum saye Lorem ipsum nipsum saye. Lorem ipsum nipsum saye Lorem ipsum nipsum saye.</p>
  </article>
  <article class="card abs" style="left:441px;top:105px">
    <div class="photo" role="img" aria-label="Person touching a digital interface screen" style="background:linear-gradient(135deg,#e9f1f6,#b7c9d6)"></div>
    <h4>Lorem ipsum nipsum saye</h4><div class="meta">Posted on: Sep 29th, 2014</div><hr>
    <p>Lorem ipsum nipsum saye Lorem ipsum nipsum saye. Lorem ipsum nipsum saye Lorem ipsum nipsum saye.</p>
  </article>
  <article class="card abs" style="left:768px;top:105px">
    <div class="photo" role="img" aria-label="Couple choosing a television in a store" style="background:linear-gradient(135deg,#7a8fa8,#2d4466)"></div>
    <h4>Lorem ipsum nipsum saye</h4><div class="meta">Posted on: Sep 29th, 2014</div><hr>
    <p>Lorem ipsum nipsum saye Lorem ipsum nipsum saye. Lorem ipsum nipsum saye Lorem ipsum nipsum saye.</p>
  </article>
</section>

<section class="band abs" style="top:1612px;height:352px">
  <h2 class="title light abs" style="top:42px">Customer Testimonials</h2>
  <div class="arrow left abs" style="left:46px;top:181px"></div>
  <div class="arrow right abs" style="left:1129px;top:181px"></div>
  <div class="video abs" style="left:88px;top:106px" role="img" aria-label="Video testimonial of a customer"><div class="play abs"></div></div>
  <div class="video abs" style="left:431px;top:106px" role="img" aria-label="Video testimonial of a customer"><div class="play abs"></div></div>
  <div class="video abs" style="left:775px;top:106px" role="img" aria-label="Video testimonial of a customer"><div class="play abs"></div></div>
</section>

<section class="abs" style="left:0;top:1964px;width:1200px;height:504px">
  <h2 class="title red abs" style="top:50px">Welcome to our Blog</h2>
  <article class="card abs" style="left:115px;top:123px">
    <div class="photo" role="img" aria-label="Technician repairing electronics" style="background:linear-gradient(135deg,#6e7f93,#2b3646)"></div>
    <h4>Lorem ipsum nipsum saye</h4><div class="meta thin">Sep 29th, 2014 / 10 Comments</div>
  </article>
  <article class="card abs" style="left:441px;top:123px">
    <div class="photo" role="img" aria-label="Hands typing on a laptop keyboard" style="background:linear-gradient(135deg,#e2e6ea,#9aa3ad)"></div>
    <h4>Lorem ipsum nipsum saye</h4><div class="meta thin">Sep 29th, 2014 / 10 Comments</div>
  </article>
  <article class="card abs" style="left:768px;top:123px">
    <div class="photo" role="img" aria-label="Young woman holding a small device" style="background:linear-gradient(135deg,#d6e9f2,#a9cfe0)"></div>
    <h4>Lorem ipsum nipsum saye</h4><div class="meta thin">Sep 29th, 2014 / 10 Comments</div>
  </article>
</section>

<footer class="footer abs">
  <div class="foot-brand abs">KESTREL</div>
  <div class="foot-links abs" style="left:99px"><span>Our Plans</span><span>Benefits</span><span>About us</span><span>Contact us</span></div>
  <div class="foot-links abs" style="left:229px"><span>Blog</span><span>News</span><span>Support</span><span>Terms</span></div>
  <div class="feed-title abs">Social Feed</div>
  <div class="social abs" style="left:602px;background:#3b5998"></div>
  <div class="social abs" style="left:643px;background:#33aadd"></div>
  <div class="social abs" style="left:684px;background:#c4302b"></div>
  <div class="feed abs">
    <div class="feed-item"><i></i><div><b>NAME OF PERSON</b><span>This is an example of post or social feed.</span></div></div>
    <div class="feed-item"><i></i><div><b>NAME OF PERSON</b><span>This is an example of post or social feed.</span></div></div>
    <div class="feed-item"><i></i><div><b>NAME OF PERSON</b><span>This is an example of post or social feed.</span></div></div>
  </div>
  <div class="contact-title abs">
    <svg width="46" height="46" viewBox="0 0 46 46"><circle cx="23" cy="23" r="21" fill="#fff"/><circle cx="23" cy="23" r="15" fill="none" stroke="#1e1e20" stroke-width="2"/><path d="M8 23 H38 M23 8 V38" stroke="#1e1e20" stroke-width="2"/></svg>
    <span>CONTACT US</span>
  </div>
  <div class="contact-rule abs"></div>
  <div class="contact-list abs">
    <div><b>EMAIL:</b> hello@bharbor.example</div>
    <div><b>CALL:</b> 555-014-2290</div>
    <div><b>ADDERESS:</b> Linden quay harbor<br>road unit no. 7</div>
  </div>
</footer>
<div class="copyright abs">Copyright © 2014 Bright Harbor Assurance</div>

</body>
</html>
```